Velmorra Design Group Business Card Design

We need a double-sided business card for our company Velmorra Design Group. Our slogan is "Simple Online Solutions." We are looking for a techy, cutting-edge but simple card that looks modern and sleek. We have a black logo attached and would prefer a lighter background to make our logo stand out. We like nice accents to make it pop out and make our clients remember our card.

On the back side, we just want our logo, slogan and website. Again, something very simple. Make the logo big on the back.

```html
<!DOCTYPE html>
<html lang="en">
<head>
<meta charset="UTF-8">
<title>Velmorra Design Group — Business Card Back</title>
<link rel="stylesheet" href="https://fonts.googleapis.com/css2?family=Arimo:wght@400;700&display=swap">
<style>
  :root {
    --ink: #111111;
    --logo-ink: #1e1e1e;
    --accent: #8a17f6;
    --bg-top: #ffffff;
    --bg-mid: #e7eaeb;
    --bg-bottom: #c2cacb;
  }

  html, body {
    margin: 0;
    padding: 0;
    width: 1200px;
    height: 857px;
    overflow: hidden;
  }

  .card {
    position: relative;
    width: 1200px;
    height: 857px;
    background: linear-gradient(to bottom, var(--bg-top) 0%, var(--bg-top) 12%, var(--bg-mid) 68%, var(--bg-bottom) 100%);
    font-family: "Arimo", Arial, sans-serif;
    overflow: hidden;
  }

  .brand-name {
    position: absolute;
    top: 124px;
    right: 70px;
    margin: 0;
    font-size: 40px;
    font-weight: 400;
    color: var(--logo-ink);
    letter-spacing: 0.5px;
    line-height: 1;
    white-space: nowrap;
  }

  .slogan {
    position: absolute;
    top: 374px;
    left: 0;
    width: 1200px;
    margin: 0;
    text-align: center;
    font-size: 88px;
    font-weight: 400;
    line-height: 1;
    color: var(--accent);
    white-space: nowrap;
    padding-right: 52px;
    box-sizing: border-box;
  }

  .slogan .initial {
    color: var(--ink);
  }

  .website {
    position: absolute;
    top: 722px;
    left: 0;
    width: 1248px;
    margin: 0;
    text-align: center;
    font-size: 47px;
    font-weight: 700;
    letter-spacing: 4px;
    line-height: 1;
    color: var(--ink);
    white-space: nowrap;
  }
</style>
</head>
<body>
  <main class="card">
    <h1 class="brand-name">Velmorra Design Group</h1>
    <p class="slogan"><span class="initial">S</span>imple <span class="initial">O</span>nline <span class="initial">S</span>olutions.</p>
    <p class="website">www.vmdg.ca</p>
  </main>
</body>
</html>
```